Orbit Crust gazebo signage project.

We are looking for signage for our mobile pizzeria gazebo structure. We sell pizza from a woodfired oven, Neapolitan style. We have a KD campervan which we sell pizza from too, which is yellow and black, so we would like to stick with those colours. The signage needs to be 2, 305cm x 76cm one for the top, and one for the bottom. It needs to state clearly the product is pizza. It also needs to include our logo, our website and that we sell Neapolitan style woodfired pizza. Our website is orbitcrust.co.uk to get a feel of our brand. We also don't want photos of pizza on the design.

Colors
000000
fbed22

Requirements
Must have
• The colours yellow and black and our logo on the top banner. Our website and the facebook, twitter and instagram logos on the bottom banner.

```html
<!DOCTYPE html>
<html lang="en">
<head>
<meta charset="utf-8">
<title>Orbit Crust – Gazebo Banners</title>
<link rel="stylesheet" href="https://fonts.googleapis.com/css2?family=Lobster&family=Open+Sans:wght@400&display=swap">
<style>
  :root {
    --canvas: #4a4a4a;
    --slate: #262626;
    --slate-light: #363636;
    --frame: #f2f2f2;
    --edge: #8a8a8a;
    --yellow: #f7c600;
    --white: #ffffff;
    --label: #ffffff;
  }
  * { box-sizing: border-box; margin: 0; padding: 0; }
  html, body { width: 925px; height: 1200px; overflow: hidden; }
  body {
    background: var(--canvas);
    font-family: "Lobster", cursive;
    position: relative;
  }
  .banner-label {
    position: absolute;
    left: 0;
    width: 86px;
    text-align: center;
    font-family: "Open Sans", sans-serif;
    font-size: 15px;
    color: var(--label);
  }
  .banner {
    position: absolute;
    left: 86px;
    width: 815px;
    height: 204px;
    border: 1px solid var(--edge);
    background: radial-gradient(ellipse at 55% 40%, var(--slate-light), var(--slate) 80%);
    overflow: hidden;
  }
  .banner-frame {
    position: absolute;
    inset: 6px;
    border: 2px solid var(--frame);
    border-radius: 12px;
    z-index: 3;
  }
  .food-area {
    position: absolute;
    top: 0;
    bottom: 0;
  }
  .top .food-left {
    left: 0; width: 240px;
    background: radial-gradient(ellipse 60% 70% at 30% 50%, rgba(70,45,38,0.55), rgba(38,38,38,0) 100%);
  }
  .top .food-right {
    right: 0; width: 220px;
    background: radial-gradient(ellipse 60% 70% at 70% 50%, rgba(70,45,38,0.55), rgba(38,38,38,0) 100%);
  }
  .bottom .food-left {
    left: 0; width: 260px;
    background: linear-gradient(90deg, #6b5644 0%, #4d3f33 45%, rgba(38,38,38,0) 100%);
  }
  .logo {
    position: absolute;
    left: 52px; top: 44px;
    width: 116px; height: 116px;
    border: 4px solid var(--white);
    border-radius: 50%;
    display: flex;
    align-items: center;
    justify-content: center;
    text-align: center;
    font-size: 22px;
    line-height: 1.05;
    color: var(--white);
    z-index: 2;
  }
  .tagline {
    position: absolute;
    left: 176px; top: 24px;
    font-size: 38px;
    line-height: 1.1;
    color: var(--white);
    z-index: 2;
  }
  .product {
    position: absolute;
    left: 174px; top: 70px;
    font-size: 86px;
    line-height: 1.1;
    color: var(--yellow);
    white-space: nowrap;
    z-index: 2;
  }
  .contact-intro {
    position: absolute;
    left: 124px; top: 32px;
    font-size: 44px;
    line-height: 1.1;
    color: var(--white);
    z-index: 2;
  }
  .web-address {
    position: absolute;
    left: 122px; top: 88px;
    font-size: 76px;
    line-height: 1.1;
    color: var(--white);
    white-space: nowrap;
    z-index: 2;
  }
  .web-address .domain { color: var(--yellow); }
  .social-dots {
    position: absolute;
    right: 54px; top: 26px;
    display: flex;
    gap: 15px;
    z-index: 2;
  }
  .social-dot {
    width: 36px; height: 36px;
    border-radius: 50%;
    background: var(--yellow);
  }
</style>
</head>
<body>

  <div class="banner-label" style="top:350px;">TOP</div>
  <section class="banner top" style="top:300px;">
    <div class="food-area food-left" role="img" aria-label="Fresh ingredients on dark slate: tomatoes, chilli, garlic, herbs and spices"></div>
    <div class="food-area food-right" role="img" aria-label="Fresh ingredients on dark slate: cherry tomatoes, garlic, olives and a spice spoon"></div>
    <div class="logo">Orbit<br>Crust</div>
    <p class="tagline">Neapolitan style</p>
    <p class="product">Woodfired Pizza</p>
    <div class="banner-frame"></div>
  </section>

  <div class="banner-label" style="top:580px;">BOTTOM</div>
  <section class="banner bottom" style="top:530px;">
    <div class="food-area food-left" role="img" aria-label="Rustic wooden board with salad leaves, cheese and cherry tomatoes"></div>
    <p class="contact-intro">Get in touch with us!</p>
    <p class="web-address">www.<span class="domain">orbitcrust</span>.co.uk</p>
    <div class="social-dots" aria-hidden="true">
      <span class="social-dot"></span>
      <span class="social-dot"></span>
      <span class="social-dot"></span>
    </div>
    <div class="banner-frame"></div>
  </section>

</body>
</html>
```